Website design for labour force (commercial truck driver) company

Looking for a Wordpress template (or design files in conjunction with a free Wordpress template).
Company tag line:
Tenvora – On Demand, Professional Drivers
Real Drivers | Real Standards | Real Results
Logo design has already been completed and is attached

Company provides contract drivers to trucking companies. Target market is both the trucking companies looking for drivers and drivers looking for work.
Design to encompass header / footer and basic page design, navigation menu, home page, contact page. Customer will add content and additional pages over time.

```html
<!DOCTYPE html>
<html lang="en">
<head>
<meta charset="utf-8">
<title>Tenvora – On Demand, Professional Drivers</title>
<link href="https://fonts.googleapis.com/css2?family=Outfit:wght@400;500;600;700;800&display=swap" rel="stylesheet">
<style>
:root{
  --green:#15876b;
  --green-dark:#0f6f57;
  --ink:#151515;
  --text:#3a3a3a;
  --muted:#6b6b6b;
  --yellow:#f5c400;
  --line:#d8d8d8;
  --white:#ffffff;
}
*{box-sizing:border-box;margin:0;padding:0}
html,body{width:1200px;height:4060px;overflow:hidden;background:var(--white)}
body{font-family:"Outfit",sans-serif;color:var(--ink)}
.page{position:relative;width:1200px;height:4060px;overflow:hidden}
.abs{position:absolute}
.photo{position:absolute}
.btn{position:absolute;display:flex;align-items:center;justify-content:space-between;padding:0 14px 0 18px;background:var(--green);color:var(--white);font-size:12px;font-weight:600;letter-spacing:.06em;text-transform:uppercase;border-radius:2px}
.btn .arrow{width:18px;height:18px;border:1px solid rgba(255,255,255,.7);border-radius:2px;display:flex;align-items:center;justify-content:center}
.accent{color:var(--green)}
h2{font-weight:600;color:var(--ink)}

/* header */
.logo{display:flex;align-items:center;gap:8px}
.logo-mark{width:30px;height:30px;border-radius:50%;background:var(--ink)}
.logo-name{font-size:24px;font-weight:700;letter-spacing:-.01em}
.logo-sub{font-size:7px;letter-spacing:.5em;color:var(--green);margin-top:-2px}
.pill{position:absolute;top:12px;height:25px;border:1px solid #222;border-radius:4px;display:flex;align-items:center;font-size:10px;font-weight:500}
.pill .ico{width:32px;height:100%;border-right:1px solid #222;display:flex;align-items:center;justify-content:center}
.pill span{padding:0 10px}
.socials{display:flex;gap:8px}
.socials i{display:block;width:12px;height:12px;border-radius:50%;background:var(--green)}
.nav{position:absolute;display:flex;gap:0;font-size:10px;font-weight:600;letter-spacing:.02em;text-transform:uppercase}
.nav a{color:var(--ink);text-decoration:none}
.nav a.on{color:var(--green)}

/* hero */
.hero{left:0;top:92px;width:1200px;height:634px;background:linear-gradient(100deg,#5d6a74 0%,#8b959c 30%,#4a4f55 55%,#7c858b 80%,#3d4248 100%)}
.hero-card{left:710px;top:240px;width:395px;height:323px;border:1.5px solid rgba(255,255,255,.85);background:rgba(40,48,56,.35);padding:40px 38px}
.hero-card h1{font-size:33px;line-height:1.08;font-weight:700;color:var(--white)}
.hero-card h1 b{color:#1ba37f;font-weight:700}
.hero-card p{margin-top:18px;font-size:13px;line-height:1.5;color:var(--white)}
.slider-bar{left:552px;top:697px;display:flex;gap:6px}
.slider-bar i{display:block;width:20px;height:3px;background:rgba(255,255,255,.6)}
.slider-bar i.on{background:var(--green)}

.frame{position:absolute;border:1.5px solid var(--ink);border-radius:2px}
.frame.green{border-color:var(--green)}
p.body{font-size:11.5px;line-height:1.42;color:var(--text)}

/* benefits */
.benefit{position:absolute;width:240px}
.benefit svg{display:block;height:58px}
.benefit h4{font-size:12px;font-weight:700;margin-top:22px}
.benefit p{font-size:11.5px;line-height:1.4;color:var(--text)}

/* clients */
.client{position:absolute;top:2654px;width:202px;height:79px;background:var(--white);box-shadow:0 6px 18px rgba(0,0,0,.08);display:flex;align-items:center;justify-content:center;font-size:22px;font-weight:700;color:var(--ink)}
.dots{left:563px;top:2774px;display:flex;gap:9px;align-items:center}
.dots i{display:block;width:5px;height:5px;border-radius:50%;background:#c8c8c8}
.dots i.on{width:13px;height:13px;border:1.5px solid var(--green);background:radial-gradient(var(--green) 35%,transparent 40%)}

/* testimonials */
.quote-card{position:absolute;top:3007px;width:368px;height:171px;border:1px solid var(--green);border-top:none;background:rgba(255,255,255,.85);padding:22px 26px 0 26px}
.quote-card p{font-size:11.5px;line-height:1.4;color:var(--text)}
.quote-card .who{margin-top:20px;font-size:11.5px;color:var(--muted)}
.qmark{position:absolute;top:2968px;font-size:110px;line-height:1;font-weight:800;color:var(--green);font-family:Georgia,serif}

/* contact */
.band{left:0;top:3545px;width:1200px;height:515px;background:var(--green)}
.contact-box{left:142px;top:3480px;width:915px;height:305px;background:var(--white);box-shadow:0 10px 30px rgba(0,0,0,.15)}
.contact-info{left:142px;top:3480px;width:401px;height:305px;background:var(--green);padding:42px 46px;color:var(--white)}
.contact-info h3{font-size:30px;line-height:1.1;font-weight:600}
.contact-info h3 b{color:var(--yellow);font-weight:700}
.ci-row{display:flex;gap:12px;align-items:flex-start;margin-top:18px;font-size:13.5px;line-height:1.35}
.ci-row svg{flex:none}
.field{position:absolute;background:#f0f0f0;font-size:12px;color:var(--ink);padding:12px 11px}
.send{left:587px;top:3712px;width:175px;height:41px;background:var(--green);color:var(--white);font-size:12px;font-weight:600;display:flex;align-items:center;justify-content:center;letter-spacing:.05em}

/* footer */
.foot-nav a{color:var(--white)}
.foot-nav a.on{color:var(--yellow)}
.foot-line{left:142px;top:3950px;width:915px;height:1px;background:rgba(255,255,255,.45)}
.copy{right:143px;top:3970px;font-size:9px;color:rgba(255,255,255,.85);letter-spacing:.02em}
</style>
</head>
<body>
<div class="page">

  <!-- Header -->
  <div class="abs logo" style="left:95px;top:22px">
    <div class="logo-mark"></div>
    <div>
      <div class="logo-name">Tenvora</div>
      <div class="logo-sub">LIMITED</div>
    </div>
  </div>

  <div class="pill" style="left:707px">
    <div class="ico"><svg width="13" height="13" viewBox="0 0 24 24" fill="none" stroke="#222" stroke-width="2"><path d="M5 3h4l2 5-2.5 1.5a11 11 0 0 0 6 6L16 13l5 2v4a2 2 0 0 1-2 2A16 16 0 0 1 3 5a2 2 0 0 1 2-2z"/></svg></div>
    <span>+64 (0)9 555 0142</span>
  </div>
  <div class="pill" style="left:866px">
    <div class="ico"><svg width="13" height="13" viewBox="0 0 24 24" fill="none" stroke="#222" stroke-width="2"><rect x="3" y="5" width="18" height="14"/><path d="M3 6l9 7 9-7"/></svg></div>
    <span>hello@tenvora.example</span>
  </div>
  <div class="abs socials" style="left:1023px;top:19px"><i></i><i></i><i></i><i></i></div>

  <nav class="nav" style="left:544px;top:57px;gap:34px">
    <a class="on">Home</a><a>About Us</a><a>Benefits of Joining Tenvora</a><a>Testimonials</a><a>Jobs</a><a>Contact</a>
  </nav>

  <!-- Hero -->
  <div class="photo hero" role="img" aria-label="Smiling truck driver in a work jacket standing in front of a row of parked trucks"></div>
  <div class="abs hero-card">
    <h1><b>Tenvora –</b><br>On Demand,<br>Professional Drivers</h1>
    <p>Tenvora specializes in providing contract drivers to trucking companies. We are run by truck drivers – for truck drivers</p>
    <div class="btn" style="position:relative;margin-top:24px;width:196px;height:36px">Contact us today <span class="arrow"><svg width="9" height="9" viewBox="0 0 10 10" stroke="#fff" stroke-width="1.4" fill="none"><path d="M2 8L8 2M3 2h5v5"/></svg></span></div>
  </div>
  <div class="abs slider-bar"><i class="on"></i><i></i><i class="on"></i></div>

  <!-- Real Drivers -->
  <div class="frame" style="left:106px;top:848px;width:443px;height:379px"></div>
  <div class="photo" style="left:95px;top:836px;width:441px;height:379px;background:linear-gradient(135deg,#7d8a95,#3f4a55 60%,#2a3440)" role="img" aria-label="Experienced truck driver in a cap and plaid shirt standing near his truck"></div>
  <div class="photo" style="left:407px;top:1074px;width:221px;height:188px;background:linear-gradient(160deg,#9aa6ad,#6b5a54 55%,#3a3e44)" role="img" aria-label="Driver at the wheel inside a truck cab"></div>

  <div class="photo" style="left:820px;top:1100px;width:380px;height:330px;background:radial-gradient(ellipse at 60% 45%,#e6e8ea 0%,#f2f3f4 45%,rgba(255,255,255,0) 72%)" role="img" aria-label="Light grey isometric illustration of a truck driving past buildings"></div>

  <h2 class="abs" style="left:695px;top:918px;font-size:29px;line-height:1.12">Real Drivers, Real<br>Standards, <span class="accent" style="font-weight:700">Real Results</span></h2>
  <p class="abs body" style="left:696px;top:1009px;width:360px">Lorem ipsum dolor sit amet, consectetur adipiscing elit, sed do eiusmod tempor incididunt ut labore et dolore magna aliqua. Ut enim ad minim veniam, quis nostrud exercitation ullamco laboris nisi ut aliquip ex ea comodo consequat. Duis aute irure dolor in reprehenderit in voluptate velit esse cillum dolore.</p>
  <div class="btn" style="left:694px;top:1109px;width:171px;height:37px">Discover more <span class="arrow"><svg width="9" height="9" viewBox="0 0 10 10" stroke="#fff" stroke-width="1.4" fill="none"><path d="M2 8L8 2M3 2h5v5"/></svg></span></div>

  <!-- Benefits -->
  <h2 class="abs" style="left:0;width:1200px;text-align:center;top:1386px;font-size:29px">Benefits of Joining <span class="accent" style="font-weight:700">Tenvora</span></h2>

  <div class="benefit" style="left:121px;top:1476px">
    <svg viewBox="0 0 60 60" width="60" fill="none" stroke="#222" stroke-width="1.6"><circle cx="22" cy="36" r="17"/><circle cx="22" cy="36" r="12" stroke="var(--green)"/><path d="M22 29v7l5 3"/><path d="M14 14h30a12 12 0 0 1 0 24h-4" stroke="var(--green)"/><path d="M48 8l6 6-6 6"/></svg>
    <h4>Continuity of work</h4>
    <p>Most of our drivers choose to stay with us long term</p>
  </div>
  <div class="benefit" style="left:456px;top:1476px">
    <svg viewBox="0 0 60 60" width="60" fill="none" stroke="#222" stroke-width="1.6"><path d="M14 4h32M14 56h32"/><path d="M18 4c0 16 22 18 22 26S18 42 18 56M42 4c0 16-22 18-22 26s22 12 22 26"/><path d="M24 50c2-4 10-4 12 0z" fill="var(--green)" stroke="var(--green)"/><path d="M8 22c-3 6-3 12 0 18M52 22c3 6 3 12 0 18" stroke="var(--green)"/></svg>
    <h4>Flexibility</h4>
    <p>Work days and hours to suit, 40-70 hours per week or hours to suit</p>
  </div>
  <div class="benefit" style="left:796px;top:1476px">
    <svg viewBox="0 0 60 60" width="60" fill="none" stroke="#222" stroke-width="1.6"><circle cx="32" cy="28" r="24"/><circle cx="32" cy="28" r="18"/><circle cx="32" cy="30" r="5"/><path d="M14 26c8-4 28-4 36 0M27 34l-6 12M37 34l6 12"/><path d="M6 44c2-6 6-10 10-10v20" stroke="var(--green)"/></svg>
    <h4>Variety</h4>
    <p>Experience &amp; exposure in different types of work and with different clients</p>
  </div>

  <div class="benefit" style="left:121px;top:1682px">
    <svg viewBox="0 0 60 60" width="60" fill="none" stroke="#222" stroke-width="1.6"><rect x="2" y="14" width="12" height="24" stroke="var(--green)"/><path d="M14 20h8l6 8v10H14"/><path d="M28 30h28v8H28"/><circle cx="10" cy="40" r="4"/><circle cx="36" cy="40" r="4"/><circle cx="48" cy="40" r="4"/></svg>
    <h4>Ongoing Training</h4>
    <p>We train drivers to Class 5</p>
  </div>
  <div class="benefit" style="left:456px;top:1682px">
    <svg viewBox="0 0 60 60" width="60" fill="none" stroke="#222" stroke-width="1.6"><rect x="2" y="4" width="34" height="46"/><circle cx="19" cy="20" r="10" stroke="var(--green)"/><path d="M19 14v12M16 17h5a2 2 0 0 1 0 4h-4a2 2 0 0 0 0 4h5" stroke="var(--green)"/><path d="M8 36h22M8 42h22M36 20h8v36H12v-6"/></svg>
    <h4>Great incentive</h4>
    <p>4 weeks paid holiday</p>
  </div>
  <div class="benefit" style="left:796px;top:1682px">
    <svg viewBox="0 0 60 60" width="60" fill="none" stroke="#222" stroke-width="1.6"><circle cx="30" cy="30" r="6" stroke="var(--green)"/><circle cx="30" cy="8" r="5"/><circle cx="30" cy="52" r="5"/><circle cx="8" cy="30" r="5"/><circle cx="52" cy="30" r="5"/><circle cx="12" cy="12" r="4" stroke="var(--green)"/><circle cx="48" cy="48" r="4" stroke="var(--green)"/><path d="M30 13v11M30 36v11M13 30h11M36 30h11"/></svg>
    <h4>Availability</h4>
    <p>Temp to permanent positions if desired</p>
  </div>

  <div class="btn" style="left:508px;top:1842px;width:183px;height:38px">Contact us now <span class="arrow"><svg width="9" height="9" viewBox="0 0 10 10" stroke="#fff" stroke-width="1.4" fill="none"><path d="M2 8L8 2M3 2h5v5"/></svg></span></div>

  <!-- Class drivers -->
  <h2 class="abs" style="left:96px;top:2118px;font-size:29px;line-height:1.12">Need Class 1, 2, 3, 4 or 5<br><span class="accent" style="font-weight:700">drivers?</span></h2>
  <p class="abs body" style="left:96px;top:2210px;width:410px">Lorem ipsum dolor sit amet, consectetur adipiscing elit, sed do eiusmod tempor incididunt ut labore et dolore magna aliqua. Ut enim ad minim veniam, quis nostrud exercitation ullamco laboris nisi ut aliquip ex ea co modo consequat. Duis aute irure dolor in reprehenderit in voluptate velit esse cillum dolore eu fugiat nulla pariatur.</p>
  <div class="btn" style="left:95px;top:2310px;width:170px;height:37px">Discover more <span class="arrow"><svg width="9" height="9" viewBox="0 0 10 10" stroke="#fff" stroke-width="1.4" fill="none"><path d="M2 8L8 2M3 2h5v5"/></svg></span></div>

  <div class="photo" style="left:0;top:2340px;width:390px;height:330px;background:radial-gradient(ellipse at 40% 50%,#e6e8ea 0%,#f2f3f4 45%,rgba(255,255,255,0) 72%)" role="img" aria-label="Light grey isometric illustration of a truck driving beside buildings"></div>

  <div class="frame" style="left:675px;top:2050px;width:443px;height:379px"></div>
  <div class="photo" style="left:662px;top:2037px;width:443px;height:379px;background:linear-gradient(135deg,#2e3238,#6a7078 45%,#a6b0b6 75%,#3b3f45)" role="img" aria-label="Young driver smiling from the seat of a truck cab"></div>
  <div class="frame green" style="left:662px;top:2037px;width:443px;height:379px;border-width:2px"></div>

  <!-- Clients -->
  <h2 class="abs" style="left:0;width:1200px;text-align:center;top:2587px;font-size:29px">Our Happy <span class="accent" style="font-weight:700">Clients</span></h2>
  <div class="client" style="left:167px">Korvane</div>
  <div class="client" style="left:388px">Bralto</div>
  <div class="client" style="left:609px">Quillar</div>
  <div class="client" style="left:829px">Morrowgate</div>
  <div class="abs dots"><i class="on"></i><i></i><i></i><i></i><i></i></div>

  <!-- Testimonials -->
  <h2 class="abs" style="left:0;width:1200px;text-align:center;top:2915px;font-size:29px">and What They <span class="accent" style="font-weight:700">Say</span></h2>
  <div class="photo" style="left:0;top:2965px;width:1200px;height:590px;background:linear-gradient(180deg,#ffffff 0%,#dfe6dc 18%,#9fb08a 42%,#7f9470 55%,#8b8f8e 70%,#5f6a5a 85%,#4d5a4a 100%)" role="img" aria-label="White truck speeding along a countryside highway with motion blur"></div>
  <div class="qmark" style="left:194px">“</div>
  <div class="qmark" style="left:607px">“</div>
  <div class="quote-card" style="left:214px">
    <p>Lorem ipsum dolor sit amet, consectetur adipiscing elit, sed do eiusmod tempor incididunt ut labore et dolore magna aliqua. Ut enim ad minim veniam, quis nostrud exercitation ullamco laboris nisi ut aliquip ex ea commo do consequat.</p>
    <div class="who">Leo Marsh</div>
  </div>
  <div class="quote-card" style="left:628px">
    <p>Lorem ipsum dolor sit amet, consectetur adipiscing elit, sed do eiusmod tempor incididunt ut labore et dolore magna aliqua. Ut enim ad minim veniam, quis nostrud exercitation ullamco laboris nisi ut aliquip ex ea commo do consequat.</p>
    <div class="who">Ivy Hollister</div>
  </div>

  <!-- Contact -->
  <div class="abs band"></div>
  <div class="abs contact-box"></div>
  <div class="abs contact-info">
    <h3>Contact Us Now and<br><b>Get Started</b></h3>
    <div class="ci-row" style="margin-top:22px"><svg width="20" height="22" viewBox="0 0 24 24" fill="none" stroke="#fff" stroke-width="1.6"><path d="M12 22s7-7 7-13a7 7 0 0 0-14 0c0 6 7 13 7 13z"/><circle cx="12" cy="9" r="2.5"/></svg><span>14 Harbourline Road<br>Westmere, 1020</span></div>
    <div class="ci-row"><svg width="20" height="20" viewBox="0 0 24 24" fill="none" stroke="#fff" stroke-width="1.6"><path d="M5 3h4l2 5-2.5 1.5a11 11 0 0 0 6 6L16 13l5 2v4a2 2 0 0 1-2 2A16 16 0 0 1 3 5a2 2 0 0 1 2-2z"/></svg><span>+64 (0)9 555 0142</span></div>
    <div class="ci-row" style="margin-top:14px"><svg width="20" height="18" viewBox="0 0 24 24" fill="none" stroke="#fff" stroke-width="1.6"><rect x="3" y="5" width="18" height="14"/><path d="M3 6l9 7 9-7"/></svg><span>hello@tenvora.example</span></div>
  </div>
  <div class="field" style="left:587px;top:3517px;width:209px;height:36px">Your Name</div>
  <div class="field" style="left:806px;top:3517px;width:208px;height:36px">Your Email</div>
  <div class="field" style="left:587px;top:3565px;width:209px;height:36px">Your Phone</div>
  <div class="field" style="left:806px;top:3565px;width:208px;height:36px">Subject</div>
  <div class="field" style="left:587px;top:3613px;width:427px;height:87px">Message</div>
  <div class="abs send">SEND</div>

  <!-- Footer -->
  <div class="abs logo" style="left:142px;top:3862px;color:var(--white)">
    <div class="logo-mark" style="background:var(--white)"></div>
    <div>
      <div class="logo-name">Tenvora</div>
      <div class="logo-sub" style="color:var(--white)">LIMITED</div>
    </div>
  </div>
  <nav class="nav foot-nav" style="left:497px;top:3875px;gap:32px;font-size:9.5px">
    <a class="on">Home</a><a>About Us</a><a>Benefits of Joining Tenvora</a><a>Testimonials</a><a>Jobs</a><a>Contact</a>
  </nav>
  <div class="abs foot-line"></div>
  <div class="abs socials" style="left:142px;top:3970px"><i style="background:#fff"></i><i style="background:#fff"></i><i style="background:#fff"></i><i style="background:#fff"></i></div>
  <div class="abs copy">© 2025 TENVORA LIMITED. ALL RIGHTS RESERVED.</div>

</div>
</body>
</html>
```